Brightmoor Co Trade Show Flyer

We need a brochure design (8.5 x 11) Info in the design (refer to rough draft I drew on Paper): "#1 selling tool to aquire new franchisees has been video testimonials" - Martin L. Greaves, C.E.O Kolva Smoothie Franchise Testimonials - Let your franchisees do the selling for you. Franchisee testimonial: $10,000 / per Franchisee Includes: • 2 minute Video • 1 minute add for your franchise's location • Concept creation • Communication with franchisee • Travel to their location • All rental equipment • 1 round of corrections • Animated logo • Licensed music ******* For 25% Discount section (next to middle box), please put the "Venture Fairground Logo" Great to use on all your social media (USE logos and icons) • Website • Reelhouse • Workweb • Gatherly • Snapframe • Chirpline • Phone calls • Emails • In person meetings Some of our clients: (use the logos I uploaded - in round boxes as in draft) LOGO (Brightmoor Franchise Testimonial) www.brightmoorstories.example (866) 555-0187

Target Market(s)

Franchise owners

Colors

Designer to choose colors to be used in the design.

Requirements

```html
<!DOCTYPE html>
<html lang="en">
<head>
<meta charset="utf-8">
<title>Brightmoor Co Trade Show Flyer</title>
<link href="https://fonts.googleapis.com/css2?family=Arimo:wght@400;700&display=swap" rel="stylesheet">
<style>
:root{
  --red:#ec3b3b;
  --ink:#222222;
  --teal:#1aa893;
  --paper:#ffffff;
  --backdrop:#c9c9c9;
}
*{box-sizing:border-box;margin:0;padding:0}
html,body{width:1200px;height:1200px;overflow:hidden;background:var(--backdrop);font-family:"Arimo",Arial,sans-serif;color:var(--ink)}
.flyer{position:absolute;left:175px;top:50px;width:850px;height:1100px;background:var(--paper);box-shadow:0 10px 24px rgba(0,0,0,.25)}
.abs{position:absolute}
.quote-box{left:22px;top:25px;width:806px;height:75px;border:1.5px solid var(--red);border-radius:4px}
.quote{left:0;width:850px;top:45px;text-align:center;font-size:22px}
.attribution{left:0;width:850px;top:87px;text-align:center}
.attribution span{background:var(--paper);color:var(--red);font-size:18px;padding:0 14px}
.title{left:0;width:850px;text-align:center;line-height:1}
.title-main{top:126px;font-size:88px;font-weight:700;letter-spacing:1px}
.title-sub{top:206px;font-size:78px;font-weight:400;color:var(--red);letter-spacing:1px}
.tagline{left:0;width:850px;top:300px;text-align:center;font-size:25px;text-transform:uppercase}
.includes{left:93px;top:354px;width:500px;height:287px;border:1.5px dashed var(--red);border-right:none;border-radius:6px 0 0 6px}
.includes ul{list-style:none;position:absolute;left:30px;top:16px}
.includes li{font-size:19px;line-height:28.4px;display:flex;align-items:center;gap:10px}
.includes svg{width:14px;height:14px}
.discount{left:592px;top:354px;width:178px;height:287px;background:var(--red);padding:14px 14px 0 16px;overflow:hidden}
.discount .music{color:#fff;font-size:22px;line-height:22px}
.discount .pct{font-size:72px;font-weight:700;line-height:74px;letter-spacing:-3px;margin-top:6px}
.discount .word{font-size:27px;line-height:30px}
.partner{left:12px;top:174px;width:154px;height:97px;background:var(--teal);color:#fff;font-size:23px;font-weight:700;line-height:26px;padding:10px 10px}
.everywhere{left:0;width:850px;top:664px;text-align:center;font-size:25px;font-weight:700;color:var(--red)}
.everywhere b{color:var(--ink)}
.channels{left:40px;width:770px;top:716px;height:52px;display:flex;justify-content:center;align-items:center;gap:18px}
.channel{display:flex;align-items:center;gap:7px;font-size:18px;font-weight:700}
.channel i{width:12px;height:12px;border-radius:50%;background:var(--ink);display:block}
.icon-ring{width:52px;height:52px;border-radius:50%;border:2px solid var(--red);display:flex;align-items:center;justify-content:center}
.icon-ring svg{width:26px;height:26px}
.clients-label{left:0;width:850px;top:798px;text-align:center;font-size:16px;font-weight:700;color:var(--red);text-transform:uppercase}
.clients{left:0;width:850px;top:840px;display:flex;justify-content:center;gap:16px}
.client{width:78px;height:78px;border-radius:50%;border:2px solid var(--red);display:flex;align-items:center;justify-content:center;text-align:center;font-size:13px;font-weight:700;line-height:15px;padding:6px}
.brand{left:90px;top:972px;width:226px;text-align:center}
.brand-name{font-size:29px;font-weight:700;letter-spacing:0;line-height:1}
.brand-sub{font-size:10px;margin-top:6px;letter-spacing:.5px}
.divider{left:332px;top:954px;width:2px;height:112px;background:var(--red)}
.phone-chip{left:356px;top:957px;width:42px;height:42px;background:var(--red);border-radius:6px;display:flex;align-items:center;justify-content:center}
.phone-number{left:414px;top:954px;font-size:46px;font-weight:700}
.globe{left:362px;top:1021px;width:22px;height:22px}
.website{left:414px;top:1020px;font-size:22px}
.footer-band{left:0;bottom:0;width:850px;height:13px;background:var(--red)}
</style>
</head>
<body>
<main class="flyer">
  <div class="abs quote-box"></div>
  <p class="abs quote">"#1 selling tool to aquire new franchisees has been video testimonials"</p>
  <p class="abs attribution"><span>Martin L. Greaves, C.E.O Kolva Smoothie</span></p>

  <h1 class="abs title title-main">FRANCHISE</h1>
  <h2 class="abs title title-sub">TESTIMONIALS</h2>
  <p class="abs tagline">Let your franchisees do the selling for you</p>

  <section class="abs includes">
    <ul>
      <li><svg viewBox="0 0 14 14"><path d="M1 7l4 4 8-10" fill="none" stroke="#ec3b3b" stroke-width="2.4"/></svg>$10,000 / per Franchisee</li>
      <li><svg viewBox="0 0 14 14"><path d="M1 7l4 4 8-10" fill="none" stroke="#ec3b3b" stroke-width="2.4"/></svg>2 minute Video</li>
      <li><svg viewBox="0 0 14 14"><path d="M1 7l4 4 8-10" fill="none" stroke="#ec3b3b" stroke-width="2.4"/></svg>1 minute add for your franchise's location</li>
      <li><svg viewBox="0 0 14 14"><path d="M1 7l4 4 8-10" fill="none" stroke="#ec3b3b" stroke-width="2.4"/></svg>Concept creation</li>
      <li><svg viewBox="0 0 14 14"><path d="M1 7l4 4 8-10" fill="none" stroke="#ec3b3b" stroke-width="2.4"/></svg>Communication with franchisee</li>
      <li><svg viewBox="0 0 14 14"><path d="M1 7l4 4 8-10" fill="none" stroke="#ec3b3b" stroke-width="2.4"/></svg>Travel to their location</li>
      <li><svg viewBox="0 0 14 14"><path d="M1 7l4 4 8-10" fill="none" stroke="#ec3b3b" stroke-width="2.4"/></svg>All rental equipment</li>
      <li><svg viewBox="0 0 14 14"><path d="M1 7l4 4 8-10" fill="none" stroke="#ec3b3b" stroke-width="2.4"/></svg>1 round of corrections</li>
      <li><svg viewBox="0 0 14 14"><path d="M1 7l4 4 8-10" fill="none" stroke="#ec3b3b" stroke-width="2.4"/></svg>Animated logo</li>
    </ul>
  </section>

  <aside class="abs discount">
    <p class="music">Licensed<br>music *******</p>
    <p class="pct">25%</p>
    <p class="word">DISCOUNT</p>
    <div class="abs partner">Venture Fairground</div>
  </aside>

  <p class="abs everywhere">USE YOUR <b>TESIMONIALS</b> EVERYWHERE</p>

  <div class="abs channels">
    <span class="channel"><i></i>Gatherly</span>
    <span class="channel"><i></i>Reelhouse</span>
    <span class="channel"><i></i>Snapframe</span>
    <span class="channel"><i></i>Chirpline</span>
    <span class="channel"><i></i>Workweb</span>
    <span class="icon-ring"><svg viewBox="0 0 26 26"><rect x="3" y="6" width="20" height="14" fill="#222"/><path d="M3 6l10 8 10-8" fill="none" stroke="#fff" stroke-width="1.5"/></svg></span>
    <span class="icon-ring"><svg viewBox="0 0 26 26"><path d="M3 10c0-4 20-4 20 0v2h-5v-2H8v2H3z" fill="#222"/><rect x="6" y="13" width="14" height="8" rx="2" fill="#222"/><circle cx="13" cy="17" r="2" fill="#fff"/></svg></span>
    <span class="icon-ring"><svg viewBox="0 0 26 26" fill="none" stroke="#222" stroke-width="1.6"><circle cx="13" cy="13" r="10"/><ellipse cx="13" cy="13" rx="4.5" ry="10"/><path d="M3 13h20M5 8h16M5 18h16"/></svg></span>
  </div>

  <p class="abs clients-label">In person meetings some of our clients:</p>
  <div class="abs clients">
    <span class="client">Scoopwell</span>
    <span class="client">DayMart</span>
    <span class="client">Kolva Smoothie</span>
    <span class="client">Cleanstar</span>
    <span class="client">Brakeline</span>
  </div>

  <div class="abs brand">
    <p class="brand-name">BRIGHTMOOR</p>
    <p class="brand-sub">— FRANCHISE TESTIMONIALS —</p>
  </div>
  <div class="abs divider"></div>
  <div class="abs phone-chip"><svg width="26" height="26" viewBox="0 0 26 26"><path d="M7 3l4 5-2.5 2.5c1.5 3 3.5 5 6.5 6.5L17.5 14.5l5 4-2.5 4c-9 0-17-8-17-17z" fill="#fff"/></svg></div>
  <p class="abs phone-number">(866) 555-0187</p>
  <svg class="abs globe" viewBox="0 0 26 26" fill="none" stroke="#ec3b3b" stroke-width="1.6"><circle cx="13" cy="13" r="11"/><ellipse cx="13" cy="13" rx="5" ry="11"/><path d="M2 13h22M4 7.5h18M4 18.5h18"/></svg>
  <p class="abs website">www.brightmoorstories.example</p>

  <div class="abs footer-band"></div>
</main>
</body>
</html>
```